English and Spanish Language School Needs a Business Card

Need a business card design a startup company called Corvella Language School. The company will offer English and Spanish conversational level courses designed to make the learner feel comfortable with grammar and vocabulary. We would like to see a logo with some colour that should communicate learning, growth.

Target Market(s)

Consumers and businesses

Industry/Entity Type

Education

Contact Information for Business Card

TBD

Font styles to use
Serif

Requirements
Must have
• Include the following
• Logo
• Name
• Title
• Cellphone Number
• Office Phone number
• Email address
• Office Address

```html
<!DOCTYPE html>
<html lang="en">
<head>
<meta charset="utf-8">
<title>Corvella Language School – Business Card</title>
<link rel="stylesheet" href="https://fonts.googleapis.com/css2?family=Tinos:wght@400;700&display=swap">
<style>
  :root {
    --brand-red: #c8202f;
    --brand-teal: #15a0ab;
    --ink: #1d1d1d;
    --card: #ffffff;
    --backdrop: #e9e7e4;
    --card-edge: #d8d6d2;
  }
  * { box-sizing: border-box; margin: 0; padding: 0; }
  html, body {
    width: 1200px; height: 900px; overflow: hidden;
    background: var(--backdrop);
    font-family: "Tinos", "Times New Roman", serif;
    color: var(--ink);
  }
  .canvas {
    position: relative; width: 1200px; height: 900px;
    display: flex; align-items: center; justify-content: center; gap: 40px;
  }
  .card {
    position: relative;
    width: 540px; height: 310px;
    background: var(--card);
    border-radius: 14px;
    border: 1px solid var(--card-edge);
  }
  .brand {
    display: flex; align-items: center; gap: 10px;
    color: var(--brand-red);
    font-weight: 700;
    line-height: 1.05;
  }
  .brand-dot {
    width: 16px; height: 16px; border-radius: 50%;
    background: var(--brand-teal); flex: none;
  }

  /* Back side */
  .card-back .brand {
    position: absolute; left: 0; right: 0; top: 105px;
    justify-content: center; font-size: 40px;
  }
  .card-back .website {
    position: absolute; left: 0; right: 0; top: 195px;
    text-align: center; font-size: 15px; letter-spacing: 0.5px;
  }

  /* Front side */
  .card-front .brand {
    position: absolute; left: 30px; top: 60px; width: 210px;
    font-size: 32px; align-items: flex-start;
  }
  .card-front .brand-dot { margin-top: 10px; }
  .divider {
    position: absolute; left: 258px; top: 40px; width: 1px; height: 230px;
    background: linear-gradient(to bottom, var(--brand-red), rgba(200,32,47,0));
  }
  .contact {
    position: absolute; left: 280px; top: 42px; right: 20px;
  }
  .contact-name {
    color: var(--brand-red); font-size: 25px; font-weight: 400; line-height: 1.1;
  }
  .contact-title { font-size: 13px; margin-bottom: 10px; }
  .contact-address { font-size: 14px; line-height: 1.35; margin-bottom: 8px; font-style: normal; }
  .contact-list { list-style: none; font-size: 14px; }
  .contact-list li { display: flex; align-items: center; gap: 8px; line-height: 1.55; }
  .contact-list svg { width: 13px; height: 13px; fill: var(--brand-red); flex: none; }
</style>
</head>
<body>
<main class="canvas">
  <section class="card card-front" aria-label="Business card front">
    <div class="brand"><span class="brand-dot"></span><span>Corvella Language School</span></div>
    <div class="divider"></div>
    <div class="contact">
      <h1 class="contact-name">Daniel Hart</h1>
      <p class="contact-title">President</p>
      <address class="contact-address">2470 Maple Avenue, Suite 400<br>Ashford, OR 97120</address>
      <ul class="contact-list">
        <li><svg viewBox="0 0 16 16"><path d="M3 1h3l1 4-2 1a9 9 0 0 0 5 5l1-2 4 1v3a2 2 0 0 1-2 2A13 13 0 0 1 1 3a2 2 0 0 1 2-2z"/></svg>(555) 214-7730</li>
        <li><svg viewBox="0 0 16 16"><path d="M4 0h8a1 1 0 0 1 1 1v14a1 1 0 0 1-1 1H4a1 1 0 0 1-1-1V1a1 1 0 0 1 1-1zm1 2v10h6V2zm3 11a1 1 0 1 0 0 2 1 1 0 0 0 0-2z"/></svg>(555) 214-7736</li>
        <li><svg viewBox="0 0 16 16"><path d="M0 3h16v10H0zm1.5 1.2V5l6.5 4 6.5-4v-.8L8 8.2z"/></svg>hello@corvellaschool.com</li>
        <li><svg viewBox="0 0 16 16"><path d="M8 0a8 8 0 1 0 0 16A8 8 0 0 0 8 0zm0 1.5c.9 0 2 2 2.2 5.5H5.8C6 3.5 7.1 1.5 8 1.5zM1.6 7h2.7c.1-2 .5-3.7 1.2-4.8A6.5 6.5 0 0 0 1.6 7zm0 2a6.5 6.5 0 0 0 3.9 4.8C4.8 12.7 4.4 11 4.3 9zm4.2 0h4.4c-.2 3.5-1.3 5.5-2.2 5.5S6 12.5 5.8 9zm5.9 0c-.1 2-.5 3.7-1.2 4.8A6.5 6.5 0 0 0 14.4 9zm2.7-2a6.5 6.5 0 0 0-3.9-4.8c.7 1.1 1.1 2.8 1.2 4.8z"/></svg>www.corvellaschool.com</li>
      </ul>
    </div>
  </section>

  <section class="card card-back" aria-label="Business card back">
    <div class="brand"><span class="brand-dot"></span><span>Corvella Language School</span></div>
    <p class="website">www.corvellaschool.com</p>
  </section>
</main>
</body>
</html>
```